Harbor Tandem Web Design Project

We need a website design for a start up company called "Harbor Tandem". We provide business consultancy services as well as technology-related services (IT). The design should communicate simplicity and elegance. The domain name of the site will be harbortandem.com. The logo of the company is https://files.pinvault.net/u/8147206/7730_2049185_31947_image.jpg
Updates

Target Market(s)

SMB, Corporates, Semi-governments, Governments.

Industry/Entity Type

Business

Requirements
Must have
• - The background of the pages should be white or soft grey, but we are open for suggestions.
- The pages should have nice menu animations.
- The pages should be "portal-style", with multiple placeholders for different sections and multiple tabs.
Nice to have
• The page should auto-fit the screen and scroll vertically as much as needed.
Should not have
• - Flash Animations.
- Generic Photos.

```html
<!DOCTYPE html>
<html lang="en">
<head>
<meta charset="utf-8">
<title>Harbor Tandem</title>
<link rel="stylesheet" href="https://fonts.googleapis.com/css2?family=Roboto+Condensed:wght@300;400&family=Arimo:wght@400;700&display=swap">
<style>
:root{
  --blue:#1a6fb4;
  --blue-dark:#1257a0;
  --red:#d8232a;
  --text:#5c5c5c;
  --muted:#8a8a8a;
  --line:#dcdcdc;
  --page:#f7f7f7;
}
*{margin:0;padding:0;box-sizing:border-box}
html,body{width:1200px;height:1122px;overflow:hidden}
body{background:#fff;font-family:"Roboto Condensed",sans-serif;color:var(--text);position:relative}
.site-header{position:absolute;left:0;top:0;width:1200px;height:150px;background:linear-gradient(#fff,#f4f4f4)}
.brand{position:absolute;left:90px;top:46px;display:flex;align-items:center;gap:12px;font-family:"Arimo",sans-serif;font-weight:700;font-size:34px;color:var(--blue)}
.brand-dot{width:26px;height:26px;border-radius:50%;background:var(--red)}
.call{position:absolute;left:700px;top:24px;font-size:23px;color:var(--blue)}
.call span{color:var(--red)}
.search{position:absolute;left:918px;top:23px;width:193px;height:27px;border:1px solid #d4d4d4;background:#fff;font-family:"Arimo",sans-serif;font-size:11px;color:#999;padding:7px 11px}
.search svg{position:absolute;right:8px;top:6px}
.main-nav{position:absolute;left:701px;top:72px;height:42px;display:flex;border:1px solid #c9c9c9;border-radius:3px;background:linear-gradient(#fdfdfd,#e6e6e6);box-shadow:0 2px 3px rgba(0,0,0,.12)}
.main-nav a{font-family:"Arimo",sans-serif;font-weight:700;font-size:14px;color:#555;text-decoration:none;line-height:40px;padding:0 15px;border-left:1px solid #d2d2d2}
.main-nav a:first-child{border-left:0;padding:0 22px;color:var(--red);background:#fafafa}
.main-nav a:hover{color:var(--blue)}
.hero{position:absolute;left:0;top:150px;width:1200px;height:357px;background:linear-gradient(160deg,#2a63b8 0%,#3b82cf 45%,#8fbbe6 75%,#dfeaf5 100%);border-bottom:4px solid var(--blue)}
.hero-text{position:absolute;left:776px;top:22px;color:#fff;font-size:31px;line-height:39px;font-weight:300}
.hero-text strong{font-weight:400}
.hero-arrow{position:absolute;top:158px;width:33px;height:33px;border-radius:50%;background:rgba(255,255,255,.75);display:flex;align-items:center;justify-content:center}
.services{position:absolute;left:90px;top:477px;width:1021px;height:215px;background:#fff;box-shadow:0 10px 14px -8px rgba(0,0,0,.2)}
.service{position:absolute;top:8px;height:197px;background:linear-gradient(90deg,#fff,#f3f3f3)}
.service h2{font-weight:400;font-size:22px;color:var(--blue);margin:3px 0 0 16px}
.service .shot{position:absolute;left:16px;top:38px;width:302px;height:121px;border:1px solid #cfe0ef}
.service .more{position:absolute;left:16px;top:172px;font-size:13px;color:var(--blue);text-decoration:none;display:flex;align-items:center;gap:9px}
.welcome{position:absolute;left:91px;top:728px;width:660px}
.welcome h1{font-weight:400;font-size:21px;color:var(--red);margin-bottom:14px}
.welcome p{font-size:15px;line-height:23px;text-align:justify}
.welcome .lead{width:410px;margin-bottom:16px}
.growth{position:absolute;left:432px;top:47px;width:230px;height:135px;background:linear-gradient(120deg,#fafafa,#e6e6e6)}
.news{position:absolute;left:786px;top:730px;width:315px;height:258px;border:1px solid #ddd;background:linear-gradient(#fafafa,#ececec);box-shadow:0 1px 3px rgba(0,0,0,.1)}
.news-icon{position:absolute;left:16px;top:14px;width:44px;height:38px;background:linear-gradient(#f2f2f2,#c9c9c9);border-radius:3px}
.news h2{position:absolute;left:69px;top:20px;font-weight:400;font-size:21px;color:var(--blue)}
.news-next{position:absolute;right:30px;top:26px;width:17px;height:17px;border-radius:50%;background:#bbb}
.news-item{position:absolute;left:17px;top:73px;width:281px;height:167px;background:#fff;padding:10px 14px}
.news-item h3{font-weight:400;font-size:15px;color:var(--red)}
.news-item time{display:block;font-size:14px;color:var(--muted);margin:13px 0 10px}
.news-item p{font-size:14px;line-height:23px;text-align:justify}
.site-footer{position:absolute;left:89px;top:1034px;width:1022px;border-top:1px solid var(--line)}
.footer-nav{margin-top:19px;font-size:15px;color:var(--muted)}
.footer-nav a{color:var(--muted);text-decoration:none}
.footer-nav i{font-style:normal;margin:0 10px}
.copyright{margin-top:14px;font-size:15px;color:var(--muted)}
.social{position:absolute;right:0;top:35px;display:flex;gap:8px}
.social span{width:24px;height:24px;border-radius:3px}
</style>
</head>
<body>
<header class="site-header">
  <div class="brand"><span class="brand-dot"></span>Harbor Tandem</div>
  <div class="call">Call us : <span>555 214 0387</span></div>
  <div class="search">Search the site...
    <svg width="18" height="14" viewBox="0 0 18 14"><path d="M1 7h14M10 2l5 5-5 5" stroke="#888" stroke-width="2" fill="none"/></svg>
  </div>
  <nav class="main-nav"><a href="#">Home</a><a href="#">About</a><a href="#">Solutions</a><a href="#">Services</a><a href="#">Contact</a></nav>
</header>

<section class="hero" role="img" aria-label="Glass globe on a pedestal against a blue sky with white clouds">
  <div class="hero-text">Consultancy for your<br><strong>BUSINESS DEVELOPMENT</strong></div>
  <span class="hero-arrow" style="left:90px"><svg width="10" height="14"><path d="M8 1L2 7l6 6" stroke="#8aa" stroke-width="1.5" fill="none"/></svg></span>
  <span class="hero-arrow" style="left:1077px"><svg width="10" height="14"><path d="M2 1l6 6-6 6" stroke="#8aa" stroke-width="1.5" fill="none"/></svg></span>
</section>

<section class="services">
  <article class="service" style="left:0;width:335px">
    <h2>Business Consultancy</h2>
    <div class="shot" role="img" aria-label="Businessman surrounded by floating screens" style="background:linear-gradient(90deg,#bfe0f6,#3b7fc0 50%,#cfe8f8)"></div>
    <a class="more" href="#"><svg width="7" height="9"><path d="M0 0v9M2 0l5 4.5L2 9z" fill="#1a6fb4" stroke="#1a6fb4"/></svg>VIEW MORE</a>
  </article>
  <article class="service" style="left:347px;width:328px">
    <h2>IT Services</h2>
    <div class="shot" role="img" aria-label="Finger touching a glowing digital interface" style="background:linear-gradient(120deg,#0f3f66,#3f8cc4 50%,#0d3a5f)"></div>
    <a class="more" href="#"><svg width="7" height="9"><path d="M0 0v9M2 0l5 4.5L2 9z" fill="#1a6fb4" stroke="#1a6fb4"/></svg>VIEW MORE</a>
  </article>
  <article class="service" style="left:685px;width:336px">
    <h2>Management Services</h2>
    <div class="shot" role="img" aria-label="Team silhouettes in front of a world map" style="background:linear-gradient(#1f5f9e,#6fa8dc 60%,#e8f2fb)"></div>
    <a class="more" href="#"><svg width="7" height="9"><path d="M0 0v9M2 0l5 4.5L2 9z" fill="#1a6fb4" stroke="#1a6fb4"/></svg>VIEW MORE</a>
  </article>
</section>

<main class="welcome">
  <h1>Welcome to our site</h1>
  <p class="lead">Donec non vestibulum purus. Vestibulum nec dapibus nulla. Ut sem sem, posuere ut euismod at, gravida non erat. Integer tristique velit id risus laoreet et ornare lacus faucibus. Vivamus eu neque et urna pharetra dapibus. Integer laoreet orci accumsan enim iaculis porttitor at at lacus. Ut mi ante, rutrum ac aliquam ut, pharetra at diam. Sed vestibulum, leo eu scelerisque luctus, felis erat placerat.</p>
  <div class="growth" role="img" aria-label="Businessman pushing up a rising bar chart"></div>
  <p>Nam non consectetur tellus. Maecenas lacinia ipsum nisl, at euismod mauris. Nunc in mauris rutrum dui eleifend molestie. Lorem ipsum dolor sit amet, consectetur adipiscing elit. In id mauris eget lectus pretium placerat nec eu lectus. Mauris a est id diam vehicula cursus. Ut volutpat volutpat libero, sit amet volutpat sem varius</p>
</main>

<aside class="news">
  <div class="news-icon" role="img" aria-label="Folded newspaper"></div>
  <h2>Latest News</h2>
  <span class="news-next"></span>
  <div class="news-item">
    <h3>Maecenas rutrum, odio nec luctus</h3>
    <time>March-8-2013</time>
    <p>Curabitur sagittis suscipit libero nec euismod. Donec elementum suscipit lorem nec fermentum. Suspendisse convallis nisi at libero auctor vestibulum id vitae dolor.</p>
  </div>
</aside>

<footer class="site-footer">
  <nav class="footer-nav"><a href="#">Home</a><i>|</i><a href="#">About us</a><i>|</i><a href="#">Solutions</a><i>|</i><a href="#">Services</a><i>|</i><a href="#">Contact us</a></nav>
  <p class="copyright">Copyright &copy; 2013 &nbsp; www.harbortandem.com &nbsp;&nbsp; All rights reserved.</p>
  <div class="social"><span style="background:#3b5b9a"></span><span style="background:#4fb3e0"></span></div>
</footer>
</body>
</html>
```